Email Banner (QuillStacks)

We require an email banner for our email promotions sent to prospect clients. The banner needs to contain the wording QuillStacks and use the same colour scheme as the logos attached.

This is for B2B professional's so needs to look like a place you would come to read technology articles.

```html
<!DOCTYPE html>
<html lang="en">
<head>
<meta charset="utf-8">
<title>QuillStacks Email Banners</title>
<link rel="stylesheet" href="https://fonts.googleapis.com/css2?family=Montserrat:ital,wght@0,700;0,800;1,400&family=Varela+Round&display=swap">
<style>
  :root {
    --stage-red: #b80000;
    --brand-red: #d60000;
    --deep-red: #c40000;
    --navy: #1c2a5c;
    --white: #ffffff;
    --photo-light: #d9d4cf;
    --photo-mid: #8a8580;
    --photo-dark: #3a3634;
  }
  * { margin: 0; padding: 0; box-sizing: border-box; }
  html, body { width: 1200px; height: 451px; overflow: hidden; }
  body {
    background: var(--stage-red);
    position: relative;
    font-family: "Varela Round", sans-serif;
    color: var(--white);
  }
  .banner {
    position: absolute;
    width: 543px;
    height: 166px;
    background: var(--brand-red);
    overflow: hidden;
    box-shadow: 0 3px 6px rgba(0,0,0,0.25);
  }
  .banner--top-left { left: 40px; top: 40px; }
  .banner--top-right { left: 618px; top: 40px; }
  .banner--bottom-left { left: 40px; top: 235px; }
  .banner--bottom-right { left: 618px; top: 235px; }

  .logo-tab {
    position: absolute;
    left: 0; top: 0;
    width: 197px; height: 52px;
    background: var(--white);
    border-bottom-right-radius: 26px;
    display: flex; align-items: center;
    padding-left: 15px;
    gap: 7px;
    z-index: 3;
  }
  .logo-mark { width: 11px; height: 11px; background: var(--brand-red); }
  .logo-name {
    font-family: "Montserrat", sans-serif;
    font-weight: 700;
    font-size: 18px;
    color: var(--navy);
  }

  .photo { position: absolute; z-index: 1; }

  .heading {
    position: absolute;
    font-family: "Montserrat", sans-serif;
    font-weight: 800;
    text-transform: uppercase;
    line-height: 1.05;
    z-index: 2;
    letter-spacing: 0.5px;
  }
  .heading .small { display: block; font-size: 17px; }
  .heading .large { display: block; font-size: 22px; }
  .subline {
    position: absolute;
    font-size: 14px;
    line-height: 1.32;
    z-index: 2;
    letter-spacing: 0.3px;
  }
  .cta {
    position: absolute;
    font-family: "Montserrat", sans-serif;
    font-weight: 800;
    text-transform: uppercase;
    border-radius: 10px;
    display: flex; align-items: center; justify-content: center;
    z-index: 2;
    letter-spacing: 0.5px;
  }
  .cta--light { background: var(--white); color: var(--brand-red); }
  .cta--solid { background: var(--deep-red); color: var(--white); }

  /* banner 1 */
  .banner--top-left .photo {
    left: 307px; top: 0; width: 236px; height: 166px;
    background: linear-gradient(120deg, var(--photo-light) 0%, #b5b0ab 45%, var(--photo-dark) 100%);
    border-bottom-left-radius: 90px 120px;
  }
  .banner--top-left .heading { left: 15px; top: 69px; }
  .banner--top-left .subline { left: 15px; top: 108px; }
  .banner--top-left .cta { left: 15px; top: 135px; width: 72px; height: 19px; font-size: 9px; border-radius: 8px; }

  /* banner 2 */
  .banner--top-right .photo {
    left: 200px; top: 0; width: 343px; height: 166px;
    background: linear-gradient(90deg, var(--brand-red) 0%, rgba(214,0,0,0.6) 30%, #8c6f6a 60%, #4a4a55 100%);
  }
  .banner--top-right .heading { left: 15px; top: 69px; }
  .banner--top-right .subline { left: 15px; top: 114px; }
  .banner--top-right .cta { left: 415px; top: 16px; width: 111px; height: 29px; font-size: 13px; }

  /* banner 3 */
  .banner--bottom-left .photo {
    left: 0; top: 52px; width: 330px; height: 114px;
    background: linear-gradient(90deg, #c9a58e 0%, #b9897a 35%, rgba(214,0,0,0.5) 75%, var(--brand-red) 100%);
  }
  .banner--bottom-left .photo-top {
    position: absolute; left: 197px; top: 0; width: 170px; height: 52px; z-index: 1;
    background: linear-gradient(90deg, #e07a7a 0%, rgba(214,0,0,0.3) 70%, var(--brand-red) 100%);
  }
  .banner--bottom-left .heading { right: 26px; top: 24px; font-size: 21px; letter-spacing: 0.8px; }
  .banner--bottom-left .subline {
    right: 26px; top: 65px; text-align: right;
    font-family: "Montserrat", sans-serif; font-style: italic; font-weight: 400;
    font-size: 17px; line-height: 1.25;
  }
  .banner--bottom-left .cta { left: 403px; top: 125px; width: 112px; height: 29px; font-size: 14px; }

  /* banner 4 */
  .banner--bottom-right .photo {
    left: 307px; top: 0; width: 236px; height: 166px;
    background: linear-gradient(135deg, #8b8a8c 0%, #a4574a 45%, #6e4a42 75%, #3d3a3a 100%);
    border-bottom-left-radius: 70px 110px;
  }
  .banner--bottom-right .heading { left: 15px; top: 64px; font-size: 29px; line-height: 0.98; letter-spacing: 1px; }
  .banner--bottom-right .subline { left: 17px; top: 122px; line-height: 1.2; }
  .banner--bottom-right .cta { left: 415px; top: 123px; width: 111px; height: 29px; font-size: 13px; }
</style>
</head>
<body>

<section class="banner banner--top-left">
  <div class="logo-tab"><span class="logo-mark"></span><span class="logo-name">QuillStacks</span></div>
  <h2 class="heading"><span class="small">Crafting Compelling</span><span class="large">Content</span></h2>
  <p class="subline">Professional Article Writing Services</p>
  <a class="cta cta--light">Click Here</a>
  <div class="photo" role="img" aria-label="Man in a grey blazer reading a book in a bright office"></div>
</section>

<section class="banner banner--top-right">
  <div class="logo-tab"><span class="logo-mark"></span><span class="logo-name">QuillStacks</span></div>
  <div class="photo" role="img" aria-label="Man in a suit writing notes at a desk beside a laptop"></div>
  <h2 class="heading"><span class="small">Crafting Compelling</span><span class="large">Content</span></h2>
  <p class="subline">How Our Article Writing Service<br>Can Boost Your Business</p>
  <a class="cta cta--solid">Click Here</a>
</section>

<section class="banner banner--bottom-left">
  <div class="logo-tab"><span class="logo-mark"></span><span class="logo-name">QuillStacks</span></div>
  <div class="photo-top"></div>
  <div class="photo" role="img" aria-label="Bearded man in an office chair holding a clipboard"></div>
  <h2 class="heading">The Power of the Pen</h2>
  <p class="subline">High-Quality Article Writing<br>is Essential for Your Brand</p>
  <a class="cta cta--light">Click Here</a>
</section>

<section class="banner banner--bottom-right">
  <div class="logo-tab"><span class="logo-mark"></span><span class="logo-name">QuillStacks</span></div>
  <div class="photo" role="img" aria-label="Woman reading papers at a desk in a brick-walled office"></div>
  <h2 class="heading">From Idea<br>to Publication</h2>
  <p class="subline">The Expert Article Writing Service<br>That Takes Your Content to the Next Level</p>
  <a class="cta cta--solid">Click Here</a>
</section>

</body>
</html>
```